Business card needed for the Rydo of Dry Cleaning!

We need a slick business card design for a new company based out of Montreal called Casiers Plimo&Zet inc. (in French) and Plimo&Zet Lockers inc. (in English). We're the Rydo of Laundry. We offer services of dry cleaning, laundry (wash&fold), minor clothing alterations, shoe repair and parcel delivery through 24/7 secured and connected lockers. Ordres are placed through our mobile application. Real time notification are sent to customers when their order is ready for pickup. The lockers will be placed throughout the downtown area, in condo and office towers, where a high density of busy people converge. It is simple, user-friendly, and most importantly convenient. We're the out of the box dry cleaner, literally.

Target Market(s)

1) Professional workers wearing suits daily
2) Campus students living in residences
3) People using laundromats
4) Families with children/yuppies who prefer to use their time doing something else than laundry

Industry/Entity Type

Dry Cleaning

Contact Information for Business Card

Name / Annick-Solène Trudel
Title / CEO & Founder
Company Name / Casiers Plimo&Zet inc. | Plimo&Zet Lockers inc.
Website www.plimozet.ca

Requirements
Must have
• Text Logo: Plimo&Zet - Nettoyeurs 24/7 Cleaners
• Logo on one side and contact info on the other (bilingual)
• Minimalist, pure design
• "We care" for your belongings feeling
• Professional, technological, clean & fresh look
Should not have
• No busy visuals. No rainbow colors.

```html
<!DOCTYPE html>
<html lang="fr">
<head>
<meta charset="utf-8">
<title>Plimo&amp;Zet – Business Card</title>
<link rel="stylesheet" href="https://fonts.googleapis.com/css2?family=Lato:wght@300;400;700&display=swap">
<style>
  :root {
    --backdrop: #e6e7e9;
    --brand-blue: #3b66b8;
    --card-white: #fbfbfb;
    --ink: #1d1d1f;
    --ink-soft: #55585e;
    --on-blue: #ffffff;
    --on-blue-soft: rgba(255, 255, 255, 0.85);
    --card-shadow: 0 18px 40px rgba(40, 50, 70, 0.18);
  }
  * { box-sizing: border-box; margin: 0; padding: 0; }
  html, body {
    width: 1200px;
    height: 801px;
    overflow: hidden;
    background: var(--backdrop);
    font-family: "Lato", sans-serif;
  }
  .canvas {
    width: 1200px;
    height: 801px;
    display: flex;
    align-items: center;
    justify-content: center;
    gap: 60px;
  }
  .card {
    width: 525px;
    height: 300px;
    border-radius: 4px;
    box-shadow: var(--card-shadow);
    position: relative;
    overflow: hidden;
  }

  /* Logo side */
  .card--front {
    background: var(--brand-blue);
    display: flex;
    flex-direction: column;
    align-items: center;
    justify-content: center;
  }
  .wordmark {
    display: flex;
    flex-direction: column;
    align-items: flex-end;
  }
  .brand-dot {
    width: 32px;
    height: 32px;
    border-radius: 50%;
    background: var(--on-blue);
    align-self: center;
    margin-bottom: 12px;
  }
  .brand-name {
    font-weight: 300;
    font-size: 58px;
    letter-spacing: -1px;
    color: var(--on-blue);
    line-height: 1;
  }
  .brand-sub {
    font-weight: 300;
    font-size: 24px;
    color: var(--on-blue);
    line-height: 1.1;
    margin-top: 2px;
  }
  .tagline {
    margin-top: 18px;
    font-weight: 400;
    font-size: 13px;
    letter-spacing: 2.5px;
    text-transform: uppercase;
    color: var(--on-blue-soft);
  }

  /* Contact side */
  .card--back {
    background: var(--card-white);
    display: flex;
    align-items: center;
    padding: 0 28px 0 30px;
  }
  .back-brand {
    width: 150px;
    flex: none;
    display: flex;
    flex-direction: column;
    align-items: center;
    text-align: center;
  }
  .back-brand__dot {
    width: 78px;
    height: 78px;
    border-radius: 50%;
    background: var(--brand-blue);
    margin-bottom: 10px;
  }
  .back-brand__name {
    font-weight: 300;
    font-size: 20px;
    color: var(--brand-blue);
    line-height: 1.1;
  }
  .back-brand__legal {
    margin-top: 8px;
    font-size: 10.5px;
    font-weight: 400;
    line-height: 1.45;
    color: var(--ink-soft);
  }
  .divider {
    width: 2px;
    height: 180px;
    flex: none;
    background: var(--brand-blue);
    margin: 0 22px 0 14px;
  }
  .contact {
    display: flex;
    flex-direction: column;
    gap: 7px;
    color: var(--ink);
  }
  .contact__name {
    font-size: 21px;
    font-weight: 300;
    white-space: nowrap;
    line-height: 1.1;
  }
  .contact__name strong { font-weight: 700; }
  .contact__title {
    font-size: 12px;
    font-weight: 400;
    color: var(--brand-blue);
    letter-spacing: 0.3px;
    margin-bottom: 6px;
    white-space: nowrap;
  }
  .contact__line {
    display: flex;
    align-items: center;
    gap: 10px;
    font-size: 15px;
    font-weight: 400;
    letter-spacing: 0.3px;
    white-space: nowrap;
  }
  .contact__icon {
    width: 13px;
    height: 13px;
    flex: none;
    fill: var(--brand-blue);
  }
</style>
</head>
<body>
  <main class="canvas">
    <section class="card card--front" aria-label="Logo side">
      <div class="wordmark">
        <span class="brand-dot"></span>
        <span class="brand-name">Plimo&amp;Zet</span>
        <span class="brand-sub">Lockers inc.</span>
      </div>
      <p class="tagline">Nettoyeurs 24/7 Cleaners</p>
    </section>

    <section class="card card--back" aria-label="Contact side">
      <div class="back-brand">
        <span class="back-brand__dot"></span>
        <span class="back-brand__name">Plimo&amp;Zet</span>
        <p class="back-brand__legal">Casiers Plimo&amp;Zet inc.<br>Plimo&amp;Zet Lockers inc.</p>
      </div>
      <span class="divider"></span>
      <div class="contact">
        <p class="contact__name"><strong>Annick-</strong>Solène Trudel</p>
        <p class="contact__title">Fondatrice &amp; PDG | CEO &amp; Founder</p>
        <p class="contact__line">
          <svg class="contact__icon" viewBox="0 0 16 16" aria-hidden="true"><path d="M1 3h14v10H1z M1 3l7 6 7-6" fill="none" stroke="#3b66b8" stroke-width="1.6"/></svg>
          annickT@plimozet.com
        </p>
        <p class="contact__line">
          <svg class="contact__icon" viewBox="0 0 16 16" aria-hidden="true"><path d="M3.5 1l3 3-1.8 1.8c.9 2 2.5 3.6 4.5 4.5L11 8.5l3 3-2 2.5C6.5 13.5 2.5 9.5 1 4z"/></svg>
          514-555-0142
        </p>
        <p class="contact__line">
          <svg class="contact__icon" viewBox="0 0 16 16" aria-hidden="true"><path d="M2 2l11 4.5-4.5 1.6L14 13.6 12.6 15 7.1 9.5 5.5 14z"/></svg>
          www.plimozet.ca
        </p>
      </div>
    </section>
  </main>
</body>
</html>
```